Halvorn spray foam and Environmental

I have business cards but need new ones. The ones I have are very bland. Here is. Y company website http://www.halvornsprayfoam.ca

Also I can send you copies of the current cards
I would also need my current logo on the new design as well.. Also spray foam and Environmental

Industry/Entity Type

Business

Logo Text

Halvorn.

```html
<!DOCTYPE html>
<html lang="en">
<head>
<meta charset="utf-8">
<title>Halvorn Spray Foam – Business Cards</title>
<link rel="stylesheet" href="https://fonts.googleapis.com/css2?family=Arimo:wght@400;700&family=EB+Garamond&display=swap">
<style>
  :root {
    --bg: #e7e6ea;
    --card: #2a2a2b;
    --purple: #7a3d97;
    --purple-soft: #8e55ad;
    --edge-gray: #77777a;
    --swoosh: #dcdce2;
    --ink: #ffffff;
    --serif-gray: #b9b9bd;
    --green: #7fd04d;
    --dot-green: #2fb34a;
  }
  * { box-sizing: border-box; margin: 0; padding: 0; }
  html, body { width: 1200px; height: 900px; overflow: hidden; }
  body {
    background: var(--bg);
    font-family: "Arimo", Arial, sans-serif;
    display: flex; justify-content: center; align-items: center; gap: 100px;
  }
  .card {
    position: relative; width: 360px; height: 630px;
    background: var(--card); overflow: hidden;
    box-shadow: 0 10px 30px rgba(0,0,0,.25);
  }
  .card-art { position: absolute; inset: 0; }
  .card-content {
    position: relative; display: flex; flex-direction: column; align-items: center;
    padding-top: 88px; text-align: center;
  }
  .brand-mark { width: 92px; height: 70px; background: var(--purple-soft); border-radius: 10px; }
  .brand-name {
    margin-top: 8px; font-weight: 700; font-size: 62px; letter-spacing: 1px;
    color: var(--purple); line-height: 1;
  }
  .division { margin-top: 14px; width: 230px; }
  .division-label { font-weight: 700; font-size: 11px; text-transform: uppercase; }
  .division-tagline {
    font-family: "EB Garamond", Georgia, serif; font-size: 21px; line-height: 1.05;
    padding-bottom: 3px; border-bottom: 2px solid;
  }
  .division--foam .division-label { color: var(--purple-soft); }
  .division--foam .division-tagline { color: var(--serif-gray); border-color: var(--purple); }
  .division--enviro .division-label,
  .division--enviro .division-tagline { color: var(--green); border-color: var(--green); }
  .contact { margin-top: 6px; color: var(--ink); font-size: 12.5px; line-height: 1.3; }
  .services {
    list-style: none; display: flex; justify-content: center; gap: 24px;
    margin-top: 10px; color: var(--ink); font-size: 12.5px;
  }
  .services li::before {
    content: ""; display: inline-block; width: 7px; height: 7px; border-radius: 50%;
    margin-right: 5px; vertical-align: 1px; background: var(--purple-soft);
  }
  .division--enviro .services li::before { background: var(--dot-green); }
  .card--back .card-content { padding-top: 110px; }
  .card--back .division { margin-top: 22px; }
</style>
</head>
<body>

<section class="card card--front" aria-label="Card front">
  <svg class="card-art" viewBox="0 0 360 630" aria-hidden="true">
    <path d="M0 0H360V16Q190 30 0 72Z" fill="var(--purple)"/>
    <path d="M0 72Q190 30 360 16" fill="none" stroke="var(--edge-gray)" stroke-width="4"/>
    <path d="M0 560Q230 525 360 395V630H0Z" fill="var(--purple)"/>
    <path d="M0 556Q230 521 360 391" fill="none" stroke="var(--edge-gray)" stroke-width="5"/>
    <path d="M0 598Q250 575 335 430Q290 570 0 616Z" fill="var(--swoosh)"/>
  </svg>
  <div class="card-content">
    <div class="brand-mark"></div>
    <div class="brand-name">HALVORN</div>
    <div class="division division--foam">
      <div class="division-label">Spray Foam Ltd.</div>
      <div class="division-tagline">Residential &amp; Commercial</div>
      <div class="contact">6045550182<br>www.halvornsprayfoam.ca<br>halvornfoam@mailbox.ca</div>
      <ul class="services"><li>Roofing foam</li><li>Slabjacking</li></ul>
    </div>
    <div class="division division--enviro">
      <div class="division-label">Environmental</div>
      <div class="division-tagline">Residential &amp; Commercial</div>
      <div class="contact">6045550347<br>www.halvornenvironmental.ca<br>enviro1@mailbox.ca</div>
      <ul class="services"><li>Air monitoring</li><li>Asbestos testing</li></ul>
    </div>
  </div>
</section>

<section class="card card--back" aria-label="Card back">
  <svg class="card-art" viewBox="0 0 360 630" aria-hidden="true">
    <path d="M0 0H360V16Q190 30 0 72Z" fill="var(--purple)"/>
    <path d="M0 72Q190 30 360 16" fill="none" stroke="var(--edge-gray)" stroke-width="4"/>
    <path d="M0 440Q240 430 360 250V630H0Z" fill="var(--purple)"/>
    <path d="M0 436Q240 426 360 246" fill="none" stroke="var(--edge-gray)" stroke-width="5"/>
    <path d="M0 490Q260 480 340 300Q300 490 0 512Z" fill="var(--swoosh)"/>
  </svg>
  <div class="card-content">
    <div class="brand-mark"></div>
    <div class="brand-name">HALVORN</div>
    <div class="division division--foam">
      <div class="division-label">Spray Foam Ltd.</div>
      <div class="division-tagline">Residential &amp; Commercial</div>
    </div>
    <div class="division division--enviro">
      <div class="division-label">Environmental</div>
      <div class="division-tagline">Residential &amp; Commercial</div>
    </div>
  </div>
</section>

</body>
</html>
```